Birthday Party Invitation

I need to create a "save the date" for my birthday party.
Text:

Save the Date
Saturday, 6 December 2014
9 pm
Club la Vereda, Lindenhofweg 42, 8005 Zürich
BLACK IT OUT
SAVE IT!
RESERVE THE TIME
WRITE IT DOWN
HOLD THE DATE to LET YOUR HAIR DOWN and Party with Me.

Target Market(s)

Friends

Industry/Entity Type

Club

Requirements
Must have
• I want the flyer to look classy and sexy at the same time.
Nice to have
• Picture on the left or right, then text white on black background. Maybe a simple frame. Not too playful, rather simple, elegant and no graphics. Just picture and text.

```html
<!DOCTYPE html>
<html lang="en">
<head>
<meta charset="utf-8">
<title>Save the Date – Birthday Party</title>
<link rel="stylesheet" href="https://fonts.googleapis.com/css2?family=Alegreya+SC&display=swap">
<style>
  :root {
    --bg: #000000;
    --ink: #ecebe6;
    --frame: #d9d9d9;
    --photo-dark: #0d0504;
    --photo-red: #5a140f;
  }
  html, body {
    margin: 0;
    padding: 0;
    width: 1200px;
    height: 800px;
    overflow: hidden;
    background: var(--bg);
  }
  .invitation {
    position: relative;
    width: 1200px;
    height: 800px;
    background: var(--bg);
    font-family: "Alegreya SC", serif;
    color: var(--ink);
  }
  .host-photo {
    position: absolute;
    left: 24px;
    top: 22px;
    width: 575px;
    height: 747px;
    border: 2px solid var(--frame);
    background: linear-gradient(to bottom, var(--photo-dark) 0%, var(--photo-red) 100%);
  }
  .details {
    position: absolute;
    left: 648px;
    top: 0;
    margin: 0;
    padding: 0;
    list-style: none;
    font-size: 17px;
    letter-spacing: 0.5px;
    line-height: 1;
  }
  .details li {
    position: absolute;
    left: 0;
    white-space: nowrap;
  }
  .details .date    { top: 79px; }
  .details .time    { top: 167px; }
  .details .venue   { top: 255px; }
  .details .line-1  { top: 342px; }
  .details .line-2  { top: 430px; }
  .details .line-3  { top: 518px; }
  .details .line-4  { top: 606px; }
  .details .closing { top: 695px; }
</style>
</head>
<body>
  <main class="invitation">
    <div class="host-photo" role="img" aria-label="Photo of the host in a festive red outfit at a party"></div>
    <ul class="details">
      <li class="date">Saturday, 6 December 2014</li>
      <li class="time">Time: 9:00 pm</li>
      <li class="venue">Club la Vereda, Lindenhofweg 42, 8005 Zürich</li>
      <li class="line-1">BLACK IT OUT</li>
      <li class="line-2">SAVE IT!</li>
      <li class="line-3">RESERVE THE TIME</li>
      <li class="line-4">WRITE IT DOWN</li>
      <li class="closing">HOLD THE DATE to LET YOUR HAIR DOWN and Party with Me.</li>
    </ul>
  </main>
</body>
</html>
```